Vitacrest gym flyer

Use the text offered in the word document and add the appropriate images in the space provided. The images may need to be resized.Can the font be bold and silver with a black outline.Can the background be light blue.I have submitted a design request for some business cards. I'd like the cards and the flyer to match.

Industry/Entity Type

Gym

```html
<!DOCTYPE html>
<html lang="en">
<head>
<meta charset="utf-8">
<title>Vitacrest gym flyer and card</title>
<link href="https://fonts.googleapis.com/css2?family=Roboto+Condensed:wght@400;700&family=Roboto:wght@700;900&display=swap" rel="stylesheet">
<style>
:root{
  --stage:#1d5d8c;
  --sky-1:#ffffff;
  --sky-2:#d8f1fa;
  --sky-3:#7fd0ec;
  --sky-4:#3aa6d8;
  --facet:#5a8fd0;
  --ink:#111111;
  --silver:#ececec;
  --caption-bg:#ffffff;
  --photo-a:#8a7a70;
  --photo-b:#c7b9ac;
  --photo-c:#5e7a4a;
  --rule:#4a86b8;
}
*{box-sizing:border-box;margin:0;padding:0}
html,body{width:1200px;height:1200px;overflow:hidden}
body{background:var(--stage);position:relative;font-family:"Roboto",Arial,sans-serif;color:var(--ink)}
.piece{position:absolute;overflow:hidden;
  background:linear-gradient(180deg,var(--sky-4) 0%,var(--sky-3) 14%,var(--sky-2) 40%,var(--sky-1) 62%,var(--sky-2) 82%,var(--sky-3) 100%);
  box-shadow:0 6px 18px rgba(0,0,0,.45)}
.facets{position:absolute;inset:0;width:100%;height:100%}
.flyer{left:30px;width:720px;height:510px}
.flyer--front{top:30px}
.flyer--back{top:630px}
.card{left:775px;top:495px;width:400px;height:229px}
.content{position:relative;text-align:center}
.silver{color:var(--silver);font-family:"Roboto Condensed",Arial,sans-serif;font-weight:700;
  -webkit-text-stroke:1px var(--ink);text-shadow:2px 2px 2px rgba(0,0,0,.5)}
.headline{font-size:44px;line-height:1;padding-top:26px;letter-spacing:-.5px}
.subhead{font-size:24px;line-height:1.2;margin-top:10px;letter-spacing:-.4px}
.results{display:flex;justify-content:center;gap:22px}
.flyer--front .results{margin-top:16px}
.flyer--back .results{margin-top:40px}
.result{position:relative;width:218px;height:193px;border:2px solid #333;box-shadow:3px 4px 6px rgba(0,0,0,.4);display:flex}
.photo{flex:1;background:linear-gradient(160deg,var(--photo-b),var(--photo-a))}
.photo + .photo{border-left:2px solid #fff}
.photo--outdoor{background:linear-gradient(160deg,#9fb29a,var(--photo-c))}
.caption{position:absolute;left:22px;bottom:-10px;width:176px;background:var(--caption-bg);
  font-family:"Roboto Condensed",Arial,sans-serif;font-weight:700;font-size:11px;padding:4px 4px;text-align:center;
  box-shadow:0 2px 3px rgba(0,0,0,.3)}
.caption small{font-weight:400;font-size:7px;margin-left:3px}
.pitch{font-family:"Roboto Condensed",Arial,sans-serif;font-weight:400;font-size:25px;line-height:1.22;margin-top:24px}
.pitch em{font-weight:700;font-style:italic}
.contact{font-family:"Roboto",Arial,sans-serif;font-weight:700;font-size:16px;line-height:1.35;margin-top:8px}
.contact--outlined{font-family:"Roboto Condensed",Arial,sans-serif;font-size:21px;line-height:1.25;margin-top:8px}
.contact--big{font-size:32px;line-height:1.1;margin-top:4px}
.stats{margin:10px 20px 0;border-top:1px solid var(--rule);padding-top:6px}
.stats h3{font-size:13px;font-weight:700}
.stats-fields{font-size:8.5px;font-weight:700;letter-spacing:.6px;margin-top:12px;white-space:nowrap}
.stats-cta{font-size:19px;font-weight:900;margin-top:6px}
.card-photo{position:absolute;left:14px;top:26px;width:150px;height:188px;
  background:linear-gradient(170deg,#b69a86,#6c5a50);border-radius:60px 60px 6px 6px}
.card-text{position:absolute;left:170px;right:10px;top:14px;text-align:center}
.card-text .headline{font-size:18px;padding-top:0;-webkit-text-stroke:.6px var(--ink)}
.card-text .subhead{font-size:11px;margin-top:4px;-webkit-text-stroke:.4px var(--ink);text-shadow:1px 1px 1px rgba(0,0,0,.5)}
.card-title{font-family:"Roboto Condensed",Arial,sans-serif;font-weight:700;font-size:22px;line-height:1.1;margin-top:22px}
.card-line{font-weight:700;font-size:9.5px;line-height:1.3;margin-top:2px}
.card-phone{font-weight:700;font-size:15px;margin-top:6px;line-height:1.3}
</style>
</head>
<body>

<section class="piece flyer flyer--front">
  <svg class="facets" viewBox="0 0 720 510" preserveAspectRatio="none" aria-hidden="true">
    <polygon points="0,0 180,0 60,110" fill="var(--facet)" opacity=".35"/>
    <polygon points="520,0 720,0 720,150" fill="var(--facet)" opacity=".35"/>
    <polygon points="620,0 720,90 720,20" fill="#ffffff" opacity=".3"/>
    <polygon points="0,360 130,510 0,510" fill="var(--facet)" opacity=".25"/>
    <polygon points="560,510 720,380 720,510" fill="var(--facet)" opacity=".25"/>
    <polygon points="0,200 200,340 0,300" fill="#ffffff" opacity=".35"/>
    <polygon points="720,230 540,340 720,320" fill="#ffffff" opacity=".35"/>
  </svg>
  <div class="content">
    <h1 class="silver headline">Are you happy with your body shape?</h1>
    <p class="silver subhead">Would you like to improve your health &amp; energy levels at the<br>same time as transforming your body shape?</p>
    <div class="results">
      <figure class="result">
        <div class="photo" role="img" aria-label="Before photo of a woman in a black dress"></div>
        <div class="photo" role="img" aria-label="After photo of the same woman, slimmer, in a black dress"></div>
        <figcaption class="caption">Kara Whitlow<small>Payroll Supervisor Age 27</small></figcaption>
      </figure>
      <figure class="result">
        <div class="photo photo--outdoor" role="img" aria-label="Before photo of a man in a grey vest in a garden"></div>
        <div class="photo" role="img" aria-label="After photo of the same man, slimmer and shirtless"></div>
        <figcaption class="caption">Glen Harper<small>Retired Police Officer Age 52</small></figcaption>
      </figure>
    </div>
    <p class="pitch">Get your body looking exactly how you<br>want it to look and more importantly... <em>KEEP IT THAT WAY</em></p>
    <p class="contact">Wellness &amp; Body Transformation Coach<br>Call Marcus for a FREE and unique body evaluation tailored to YOU.<br>07700 900 482 Friendbook: Marcus Hale</p>
  </div>
</section>

<section class="piece flyer flyer--back">
  <svg class="facets" viewBox="0 0 720 510" preserveAspectRatio="none" aria-hidden="true">
    <polygon points="0,0 220,0 80,90" fill="var(--facet)" opacity=".35"/>
    <polygon points="480,0 720,0 720,120" fill="var(--facet)" opacity=".35"/>
    <polygon points="0,40 150,0 0,120" fill="#ffffff" opacity=".3"/>
    <polygon points="0,380 120,510 0,510" fill="var(--facet)" opacity=".25"/>
    <polygon points="600,510 720,400 720,510" fill="var(--facet)" opacity=".25"/>
    <polygon points="0,190 190,320 0,290" fill="#ffffff" opacity=".35"/>
    <polygon points="720,210 530,330 720,300" fill="#ffffff" opacity=".35"/>
  </svg>
  <div class="content">
    <div class="results">
      <figure class="result">
        <div class="photo" role="img" aria-label="Before photo of a woman holding a baby"></div>
        <div class="photo" role="img" aria-label="After photo of the same woman, slimmer, in black"></div>
        <figcaption class="caption">Amy Dorset<small>Beautician Age 35</small></figcaption>
      </figure>
      <figure class="result">
        <div class="photo" role="img" aria-label="Before photo of a man shirtless in shorts"></div>
        <div class="photo" role="img" aria-label="After photo of the same man, leaner, shirtless"></div>
        <figcaption class="caption">Rob Fenwick<small>Sports Therapist Age 35</small></figcaption>
      </figure>
    </div>
    <p class="pitch">Get your body looking exactly how you<br>want it to look and more importantly... <em>KEEP IT THAT WAY</em></p>
    <p class="silver contact contact--outlined">Wellness &amp; Body Transformation Coach<br>Call Marcus for a FREE and unique body evaluation tailored to YOU.</p>
    <p class="silver contact--big">07700 900 482 Friendbook: Marcus Hale</p>
    <div class="stats">
      <h3>Your Stats:</h3>
      <p class="stats-fields">Weight:............... Body Fat %:.............. Metabolic Age: .............. Muscle Mass %:.............. Water Hydration: ..............</p>
      <p class="stats-cta">Don't like your stats? Call Marcus 07700 900 482 Today.</p>
    </div>
  </div>
</section>

<section class="piece card">
  <svg class="facets" viewBox="0 0 400 229" preserveAspectRatio="none" aria-hidden="true">
    <polygon points="0,0 120,0 30,60" fill="var(--facet)" opacity=".35"/>
    <polygon points="300,0 400,0 400,70" fill="var(--facet)" opacity=".35"/>
    <polygon points="400,160 300,229 400,229" fill="var(--facet)" opacity=".25"/>
    <polygon points="0,229 80,229 0,170" fill="var(--facet)" opacity=".25"/>
  </svg>
  <div class="card-photo" role="img" aria-label="Athletic woman and man in sportswear crouching together"></div>
  <div class="card-text">
    <h2 class="silver headline">Are you happy with your body shape?</h2>
    <p class="silver subhead">Would you like to improve your health &amp; energy levels<br>at the same time as transforming your body shape?</p>
    <p class="card-title">Wellness &amp;<br>Body Transformation Coach</p>
    <p class="card-line">Call Marcus for a FREE and unique body<br>evaluation tailored to YOU.</p>
    <p class="card-phone">07700 900 482<br>Friendbook: Marcus Hale</p>
  </div>
</section>

</body>
</html>
```